Website for virtual assistant and proofreader

Professional, feminine (but not flowery!) website offering and explaining my services as a VA and Proofreader. Probably only 7 pages: home, about, services (x2), fees, testimonials and contact page. <br/><br/>I already have most of the content, which I have uploaded so you can get an idea of waht I do. I have brand colours and logo already also uploaded. I really just need the bones of the site to be designed and am happy/capable of setting this up as a Wordpress site. I'm just rubbish at design!

Industry/Entity Type

Business Service

Coding

Coded - Design and coding required

Number of Pages Required

4 page

Other font styles liked:
• Roboto Bold + Great Vibes

Colors
3276b5
fee3d4

Requirements
Must have
• should be informative, professional, feminine. Clean, clear, CTA's links to services and fees pages
• Also, see all 3 colour codes on the attached doc.
Nice to have
• business images but place holders will do
Should not have
• Nothing flowery or cartoons! Not 'busy'

```html
<!DOCTYPE html>
<html lang="en">
<head>
<meta charset="utf-8">
<title>Maren T Holloway – Virtual Assistant and Proofreader</title>
<link href="https://fonts.googleapis.com/css2?family=Great+Vibes&family=Roboto:wght@400;500;700&display=swap" rel="stylesheet">
<style>
:root{
  --blue:#1f6695;
  --blue-deep:#155a86;
  --cert-blue:#2470a0;
  --ink:#333;
  --text:#4a4a4a;
  --muted:#8a8a8a;
  --taupe:#8b7f7d;
  --footer:#232323;
  --footer-line:#3a3a3a;
  --star:#f39c12;
  --white:#fff;
}
*{box-sizing:border-box;margin:0;padding:0}
html,body{width:1200px;height:3561px;overflow:hidden}
body{position:relative;background:var(--white);font-family:'Roboto',Arial,sans-serif;color:var(--text)}
.script{font-family:'Great Vibes',cursive;font-weight:400;color:var(--blue)}
.btn{position:absolute;background:var(--blue-deep);color:#fff;font:700 10px 'Roboto',sans-serif;letter-spacing:.3px;display:flex;align-items:center;justify-content:center;text-transform:uppercase}

/* header */
.site-header{position:absolute;left:0;top:0;width:1200px;height:115px;border-top:3px solid var(--blue)}
.brand{position:absolute;left:240px;top:44px}
.brand-name{font:500 22px 'Roboto',sans-serif;color:var(--blue)}
.brand-tag{font:500 9px 'Roboto',sans-serif;color:var(--blue);margin-top:2px}
.contact-chip{position:absolute;top:30px;display:flex;gap:10px;align-items:center}
.chip-icon{width:31px;height:31px;border:1px solid #cfd8df;border-radius:4px;display:flex;align-items:center;justify-content:center}
.chip-label{font:700 10px 'Roboto',sans-serif;color:var(--ink)}
.chip-value{font:500 11.5px 'Roboto',sans-serif;color:var(--blue)}
.main-nav{position:absolute;top:77px;left:575px;font:700 9px 'Roboto',sans-serif;color:var(--ink)}
.main-nav span{position:absolute;white-space:nowrap}
.main-nav .active{color:var(--blue)}

/* hero */
.hero{position:absolute;left:0;top:115px;width:1200px;height:502px;background:linear-gradient(100deg,#4f5a45 0%,#7d8670 30%,#b8aa9a 55%,#cfc7bd 75%,#9c978f 100%)}
.hero-title{position:absolute;left:235px;top:170px;font-size:62px;color:#fff;line-height:1}
.hero-sub{position:absolute;left:235px;top:238px;font:700 19px 'Roboto',sans-serif;color:#fff}

/* welcome */
.welcome-title{position:absolute;left:233px;top:672px;font-size:44px;line-height:1}
.welcome-text{position:absolute;left:235px;top:731px;width:378px;font-size:9.4px;line-height:11.4px;color:var(--text)}
.welcome-text p{margin-bottom:11px}
.portrait{position:absolute;left:654px;top:682px;width:312px;height:425px;background:linear-gradient(160deg,#c9a78a,#a5715a 55%,#7c4e3c)}

/* services */
.services-band{position:absolute;left:0;top:1171px;width:1200px;height:200px;background:var(--taupe)}
.services-title{position:absolute;left:0;width:1200px;top:1200px;text-align:center;font-size:44px;color:#fff;line-height:1}
.services-intro{position:absolute;left:270px;width:660px;top:1261px;text-align:center;color:#fff;font-size:9.6px;line-height:16px}
.service{position:absolute;top:1341px;width:180px;text-align:center}
.service-icon{width:60px;height:60px;margin:0 auto;border-radius:50%;background:#fff;border:2px solid #d9d3d1;display:flex;align-items:center;justify-content:center}
.service-title{margin-top:16px;font:500 11.5px 'Roboto',sans-serif;color:var(--ink);line-height:19px}
.service-desc{margin-top:4px;font-size:9.6px;color:var(--text);line-height:16px}
.service-link{display:inline-block;margin-top:6px;font:700 8px 'Roboto',sans-serif;color:var(--blue);text-decoration:underline}

.tagline{position:absolute;left:0;width:1200px;top:1560px;text-align:center;font-size:36px;font-weight:400;line-height:1}

/* why me */
.photo-desk{position:absolute;left:0;top:1648px;width:600px;height:485px;background:linear-gradient(135deg,#f3f3f5,#e4e4e8 50%,#cfd0d6)}
.why-col{position:absolute;left:654px;width:496px}
.why-col h3{font-size:28px;line-height:1;margin-bottom:10px}
.why-col p{font-size:9.4px;line-height:11.6px;color:var(--text);margin-bottom:11px}

/* calling */
.calling{position:absolute;left:61px;top:2170px;width:498px}
.calling h3{font-size:28px;line-height:1;margin-bottom:16px}
.calling p{font-size:9.4px;line-height:11.6px;color:var(--text);margin-bottom:11px}
.photo-notebook{position:absolute;left:600px;top:2133px;width:600px;height:530px;background:linear-gradient(160deg,#f0f0ef 0%,#e6c4a6 40%,#e79a3a 70%,#d88a2e 100%)}

/* certifications */
.certs{position:absolute;left:0;top:2663px;width:1200px;height:226px;background:var(--cert-blue)}
.certs h2{position:absolute;left:0;width:1200px;top:43px;text-align:center;font:700 15.5px 'Roboto',sans-serif;color:#fff}
.cert{position:absolute;font:500 9.4px 'Roboto',sans-serif;color:#fff;display:flex;align-items:center;gap:8px;white-space:nowrap}

/* testimonials */
.testi-title{position:absolute;left:0;width:1200px;top:2925px;text-align:center;font-size:32px;line-height:1}
.card{position:absolute;top:2983px;width:233px;height:183px;border:1px solid #e6e6e6;background:#fff;padding:20px 21px}
.card-top{display:flex;justify-content:space-between;align-items:center}
.quote-mark{font:700 22px 'Roboto',sans-serif;color:var(--ink);line-height:1}
.stars{display:flex;gap:4px}
.card-text{margin-top:10px;font-size:9.4px;line-height:15px;color:var(--muted)}
.card-person{display:flex;align-items:center;gap:13px;margin-top:18px}
.avatar{width:46px;height:46px;border-radius:50%;background:linear-gradient(135deg,#c9c3bc,#7d7871)}
.person-name{font:700 11px 'Roboto',sans-serif;color:var(--ink)}
.person-role{font-size:9.5px;color:var(--blue);margin-top:4px}
.dots{position:absolute;top:3194px;left:564px;display:flex;gap:5px}
.dots span{width:22px;height:2px;background:#9bb7cc}
.dots .on{background:var(--blue)}

/* footer */
.site-footer{position:absolute;left:0;top:3242px;width:1200px;height:319px;background:var(--footer)}
.subscribe-input{position:absolute;left:234px;top:33px;width:208px;height:32px;background:#3b3b3b;color:#8a8a8a;font-size:9px;padding:11px 12px}
.subscribe-btn{left:449px;top:33px;width:97px;height:32px;font-size:9px}
.social{position:absolute;top:42px;width:20px;height:20px;border-radius:50%;background:#3b3b3b}
.foot-brand{position:absolute;left:234px;top:126px}
.foot-brand .brand-name{color:#fff;font-size:19px}
.foot-brand .brand-tag{color:#fff;font-size:7.5px}
.foot-contact{position:absolute;left:234px;top:181px;font-size:8.5px;color:#bdbdbd;line-height:20px}
.foot-contact b{color:#fff;font-weight:500}
.foot-col{position:absolute;top:130px}
.foot-col h4{font:700 10px 'Roboto',sans-serif;color:#fff;margin-bottom:12px;text-transform:uppercase}
.foot-col li{list-style:none;font-size:8.5px;color:#9a9a9a;line-height:17.5px}
.foot-rule{position:absolute;left:234px;top:262px;width:732px;height:1px;background:var(--footer-line)}
.copyright{position:absolute;left:0;width:1200px;top:287px;text-align:center;font-size:8.3px;color:#9a9a9a}
.copyright b{color:#fff;font-weight:500}
</style>
</head>
<body>

<header class="site-header">
  <div class="brand">
    <div class="brand-name">Maren T Holloway</div>
    <div class="brand-tag">Virtual Assistant and Proofreader</div>
  </div>
  <div class="contact-chip" style="left:688px">
    <div class="chip-icon"><svg width="14" height="11" viewBox="0 0 14 11"><rect x="0.5" y="0.5" width="13" height="10" rx="1" fill="var(--blue)"/><path d="M1 1l6 5 6-5" fill="none" stroke="#fff" stroke-width="1.2"/></svg></div>
    <div><div class="chip-label">Email Us:</div><div class="chip-value">maren@hollowayva.net</div></div>
  </div>
  <div class="contact-chip" style="left:842px">
    <div class="chip-icon"><svg width="13" height="13" viewBox="0 0 24 24"><path fill="var(--blue)" d="M6.6 10.8a15.2 15.2 0 006.6 6.6l2.2-2.2a1 1 0 011-.25 11.4 11.4 0 003.6.57 1 1 0 011 1V20a1 1 0 01-1 1A17 17 0 013 4a1 1 0 011-1h3.5a1 1 0 011 1c0 1.25.2 2.45.57 3.6a1 1 0 01-.25 1z"/></svg></div>
    <div><div class="chip-label">Call Us:</div><div class="chip-value">+66 80 412 7750</div></div>
  </div>
  <nav class="main-nav">
    <span class="active" style="left:0">HOME</span>
    <span style="left:48px">SERVICES</span>
    <span style="left:115px">SYSTEM APPLICATIONS</span>
    <span style="left:241px">FEES</span>
    <span style="left:285px">WHY ME?</span>
    <span style="left:348px">CONTACT</span>
  </nav>
</header>

<section class="hero" role="img" aria-label="Photo of a smiling woman writing notes beside a laptop in a bright office">
  <div class="hero-title script">Allow me...</div>
  <div class="hero-sub">to handle the details so you can get on with business.</div>
  <div class="btn" style="left:235px;top:282px;width:124px;height:32px">Learn More</div>
</section>

<section>
  <h2 class="welcome-title script">Welcome</h2>
  <div class="welcome-text">
    <p>Every great leader is backed by diligent and knowledgeable support. Have you ever wondered what it would be like to have your very own personal assistant? Well, you can. A virtual assistant can do everything a full-time assistant can, with the added bonus that she can save you money. Whether you need daily help, or help with special assignments or big projects, hiring me as your VA will save you the costs typically associated with an employee–holiday pay, sick pay, overtime, taxes, and insurance, are no longer your concern. And, as a virtual assistant, I only charge for the hours I actually work–no more resource-siphoning downtime.</p>
    <p>Allow me to be of service. Answering emails, organizing client files, managing projects, updating website content, proofreading content, they are all important tasks but not so important that you have to do them yourself. I have rescued many businesses from the throws of chaos, bringing order to a seemingly endless onslaught of details and procedures. I can make your business function optimally. And as an independent agent, I can do it for a fraction of the cost of a full-time right-hand assistant.</p>
    <p>From organizing existing businesses to creating systems and procedures to launching a fledgling business, I offer decades of experience mastering the minutiae so your business can function at its optimum.</p>
    <p>So trust your important tasks to a professional specially qualified to handle the mundane and minutiae. Delegate to an expert and restore the life-work balance that will benefit you, your clients, and your personal relationships.</p>
    <p>Isn't it time you hire the right-hand support your business needs and you deserve?</p>
  </div>
  <div class="btn" style="left:234px;top:1069px;width:125px;height:33px">Learn More</div>
  <div class="portrait" role="img" aria-label="Portrait photo of the virtual assistant"></div>
</section>

<section>
  <div class="services-band"></div>
  <h2 class="services-title script">Our Services</h2>
  <p class="services-intro">Do you need some Smart Office Support (SOS)? Do you have a huge project looming on the horizon? Do you just need a little support managing the growing stacks of To-Dos cluttering your desk? As a master of managing the barrage of daily details that require concise and prompt attention, SOS is my speciality, from organisation to proofreading, no detail is too small!</p>

  <div class="service" style="left:228px">
    <div class="service-icon"><svg width="28" height="28" viewBox="0 0 28 28" fill="none" stroke="var(--blue)" stroke-width="1.4"><circle cx="14" cy="8" r="3"/><circle cx="6" cy="10" r="2.5"/><circle cx="22" cy="10" r="2.5"/><path d="M9 22v-4a5 5 0 0110 0v4M2 22v-3a4 4 0 017-2M26 22v-3a4 4 0 00-7-2"/></svg></div>
    <div class="service-title">Organizational/Project<br>Management</div>
    <div class="service-desc">Reliable project and team management, master of organisation</div>
    <span class="service-link">Learn More</span>
  </div>
  <div class="service" style="left:416px">
    <div class="service-icon"><svg width="28" height="28" viewBox="0 0 28 28" fill="none" stroke="var(--blue)" stroke-width="1.4"><rect x="5" y="3" width="18" height="22" rx="1"/><rect x="8" y="6" width="12" height="5"/><path d="M9 15h2M13 15h2M17 15h2M9 19h2M13 19h2M17 19h2"/></svg></div>
    <div class="service-title">Administrative and<br>Accounting Support</div>
    <div class="service-desc">Work smarter not harder with the right VA by your side</div>
    <span class="service-link">Learn More</span>
  </div>
  <div class="service" style="left:604px">
    <div class="service-icon"><svg width="28" height="28" viewBox="0 0 28 28" fill="none" stroke="var(--blue)" stroke-width="1.4"><rect x="3" y="5" width="22" height="15" rx="1"/><path d="M3 9h22M10 24h8M14 20v4"/><circle cx="14" cy="14.5" r="3"/></svg></div>
    <div class="service-title">Website<br>Administration</div>
    <div class="service-desc">Dependable and reliable website updates–like clockwork</div>
    <span class="service-link">Learn More</span>
  </div>
  <div class="service" style="left:792px">
    <div class="service-icon"><svg width="28" height="28" viewBox="0 0 28 28" fill="none" stroke="var(--blue)" stroke-width="1.4"><path d="M5 3h13l4 4v18H5z"/><path d="M8 9h8M8 13h6"/><circle cx="16" cy="18" r="3.5"/><path d="M18.5 20.5l4 4"/></svg></div>
    <div class="service-title">Editorial Service<br>/Proofreading</div>
    <div class="service-desc">Catching simple typos and grammatical faux pas to preserve your integrity</div>
    <span class="service-link">Learn More</span>
  </div>

  <h2 class="tagline script">If you want something done right... find the right person to do it!</h2>
</section>

<section>
  <div class="photo-desk" role="img" aria-label="Photo of a hand writing in a notebook beside a keyboard"></div>
  <div class="why-col" style="top:1665px">
    <h3 class="script">Why Me?</h3>
    <p>I offer administrative, management, and editorial services for those in need of an expert, professional, and discreet "virtual" assistant. As an independent contractor, I can offer you these services with all the same dedication and loyalty as a full-time staff assistant – at a more cost-effective rate.</p>
  </div>
  <div class="why-col" style="top:1778px">
    <h3 class="script">Who's benefited from my help...</h3>
    <p>My employers and clients hail from backgrounds in marketing, education, import/export businesses, IT, health and wellbeing and hospitality. They range from small to large businesses and individuals, all with a common issue – they needed help managing the day-to-day details that make their operations run smoothly. There is no job too big or too small.</p>
    <p>My clients are entrepreneurs, consultants, charitable organisations, small businesses, students and professors – all of whom can attest to the benefits of outsourcing time-consuming tasks that distract them from their primary mission.</p>
  </div>
  <div class="why-col" style="top:1940px">
    <h3 class="script">What I can do for you...</h3>
    <p>Sales accounting, inventory control, social media management, general office support, marketing assistance, client or HR relations, project management, contract reviews, regulatory compliance documentation ... essentially any area of business that can benefit from administrative support, you'll find I can deliver exemplary service. There is no job too big or too small.</p>
    <p>And, as of 2019, I am proud to announce that I am expanding my services to offer editorial services after completing my Professional Certificate for Proofreading. I look forward to offering this service to business and individuals who prepare proposals, investor reports, academic papers, grant writers, and even blog posts and web pages. Let me put the perfect polish on your public prose.</p>
  </div>
</section>

<section>
  <div class="calling">
    <h3 class="script">Sometimes your calling... well, it finds you!</h3>
    <p>I have over 30-years experience rescuing countless businesses from backlogs of work or faulty practices, and I have helped launched almost as many new businesses by building a solid foundation on sound systems. I have a history of arriving in just the right place at just the right time – when businesses and professionals need me the most.</p>
    <p>I have fine-tuned my administration skills and operational and organisational insights over three decades, starting in a local government office in the UK. Over the course of those years, I have amassed experience in accounting, stock purchasing and management, IT support (research, purchase, installation, and maintenance of software), personnel training and management, general PA duties, business compliance (insurance, fire, health &amp; safety regulations), contract management, and human resources services – skills built on a strong foundation of office and administrative expertise.</p>
    <p>After many years in the corporate world as a customer service representative, I landed in the import/export business, coordinating stock production with China (in association with the APAC Operations Director) for distribution throughout the UK, Europe, South Africa, South America, and the USA. Under the Managing Director, I prepared weekly, monthly, and quarterly financial reports for distribution to stakeholders as well as staff. I managed a team effort to plan, coordinate and provide seminars, exhibitions, marketing campaigns, and product launches.</p>
    <p>Before embarking on my own, I was the go-to gal for Word Harbour, a language school in Thailand, instituting new software systems and procedures to streamline and expedite the management of student records and government compliances documentation (Visas). I managed the school's website development and daily administration, directed email marketing campaigns and liaised with the public, students and businesses, providing a unified image to our community, our target market.</p>
    <p>I am conscientious, meticulous, methodical, diligent and driven. I am a strategic thinker, skilled at organisation and plan execution. I love a challenge and am continually learning new applications and platforms to help me deliver on my promises to you.</p>
    <p>With my help, you never have to wonder if your project will be completed on time or to your standards. I have a very hands-on approach involvement with my clients, their projects and their businesses.</p>
    <p>Allow me to assist you and restore your work-life balance.</p>
  </div>
  <div class="photo-notebook" role="img" aria-label="Photo of a woman in an orange top writing in a notebook beside a plant"></div>
</section>

<section class="certs">
  <h2>CERTIFICATIONS AND QUALIFICATIONS</h2>
  <div class="cert" style="left:384px;top:83px"><svg width="10" height="8" viewBox="0 0 10 8"><path d="M1 4l3 3 5-6" fill="none" stroke="#fff" stroke-width="1.3"/></svg>Professional Certificate for Proofreading</div>
  <div class="cert" style="left:384px;top:106px"><svg width="10" height="8" viewBox="0 0 10 8"><path d="M1 4l3 3 5-6" fill="none" stroke="#fff" stroke-width="1.3"/></svg>Diploma for Wordcraft and Gridsheet</div>
  <div class="cert" style="left:384px;top:129px"><svg width="10" height="8" viewBox="0 0 10 8"><path d="M1 4l3 3 5-6" fill="none" stroke="#fff" stroke-width="1.3"/></svg>Thai language – A1</div>
  <div class="cert" style="left:384px;top:152px"><svg width="10" height="8" viewBox="0 0 10 8"><path d="M1 4l3 3 5-6" fill="none" stroke="#fff" stroke-width="1.3"/></svg>Spanish to GCSE Level – A1</div>
  <div class="cert" style="left:384px;top:175px"><svg width="10" height="8" viewBox="0 0 10 8"><path d="M1 4l3 3 5-6" fill="none" stroke="#fff" stroke-width="1.3"/></svg>Northvale Book-keeping Stage 1</div>
  <div class="cert" style="left:610px;top:83px"><svg width="10" height="8" viewBox="0 0 10 8"><path d="M1 4l3 3 5-6" fill="none" stroke="#fff" stroke-width="1.3"/></svg>Qualified TEFL teacher</div>
  <div class="cert" style="left:610px;top:106px"><svg width="10" height="8" viewBox="0 0 10 8"><path d="M1 4l3 3 5-6" fill="none" stroke="#fff" stroke-width="1.3"/></svg>Crestfield Awards in Public House Management</div>
  <div class="cert" style="left:610px;top:129px"><svg width="10" height="8" viewBox="0 0 10 8"><path d="M1 4l3 3 5-6" fill="none" stroke="#fff" stroke-width="1.3"/></svg>6 C.S.E. Grade 3 and above, 2 'O' Levels</div>
  <div class="cert" style="left:610px;top:152px"><svg width="10" height="8" viewBox="0 0 10 8"><path d="M1 4l3 3 5-6" fill="none" stroke="#fff" stroke-width="1.3"/></svg>Many other online courses</div>
</section>

<section>
  <h2 class="testi-title script">Testimonials</h2>
  <article class="card" style="left:234px">
    <div class="card-top"><span class="quote-mark">”</span><div class="stars"><svg width="80" height="12" viewBox="0 0 80 12" fill="var(--star)"><path id="st" d="M6 0l1.8 3.8 4.2.5-3.1 2.9.8 4.2L6 9.3 2.3 11.4l.8-4.2L0 4.3l4.2-.5z"/><use href="#st" x="17"/><use href="#st" x="34"/><use href="#st" x="51"/><use href="#st" x="68"/></svg></div></div>
    <p class="card-text">Lorem ipsum dolor sit amet, consectetur adipiscing elit. Quisque iaculis elementum eleifend. Cras malesuada vitae enim id imperdiet. Vestibulum vestibulum egestas.</p>
    <div class="card-person"><div class="avatar" role="img" aria-label="Client photo"></div><div><div class="person-name">TOBIAS RENNER</div><div class="person-role">Client</div></div></div>
  </article>
  <article class="card" style="left:484px">
    <div class="card-top"><span class="quote-mark">”</span><div class="stars"><svg width="80" height="12" viewBox="0 0 80 12" fill="var(--star)"><use href="#st"/><use href="#st" x="17"/><use href="#st" x="34"/><use href="#st" x="51"/><use href="#st" x="68"/></svg></div></div>
    <p class="card-text">Lorem ipsum dolor sit amet, consectetur adipiscing elit. Quisque iaculis elementum eleifend. Cras malesuada vitae enim id imperdiet. Vestibulum vestibulum egestas.</p>
    <div class="card-person"><div class="avatar" role="img" aria-label="Client photo"></div><div><div class="person-name">TOBIAS RENNER</div><div class="person-role">Client</div></div></div>
  </article>
  <article class="card" style="left:733px">
    <div class="card-top"><span class="quote-mark">”</span><div class="stars"><svg width="80" height="12" viewBox="0 0 80 12" fill="var(--star)"><use href="#st"/><use href="#st" x="17"/><use href="#st" x="34"/><use href="#st" x="51"/><use href="#st" x="68"/></svg></div></div>
    <p class="card-text">Lorem ipsum dolor sit amet, consectetur adipiscing elit. Quisque iaculis elementum eleifend. Cras malesuada vitae enim id imperdiet. Vestibulum vestibulum egestas.</p>
    <div class="card-person"><div class="avatar" role="img" aria-label="Client photo"></div><div><div class="person-name">TOBIAS RENNER</div><div class="person-role">Client</div></div></div>
  </article>
  <div class="dots"><span class="on"></span><span></span><span></span></div>
</section>

<footer class="site-footer">
  <div class="subscribe-input">Enter your email...</div>
  <div class="btn subscribe-btn">Subscribe</div>
  <div class="social" style="left:886px"></div>
  <div class="social" style="left:915px"></div>
  <div class="social" style="left:944px"></div>

  <div class="foot-brand">
    <div class="brand-name">Maren T Holloway</div>
    <div class="brand-tag">Virtual Assistant and Proofreader</div>
  </div>
  <div class="foot-contact">Phone: <b>+66 80 412 7750</b><br>Email: <b>maren@hollowayva.net</b></div>

  <div class="foot-col" style="left:434px"><h4>Services</h4><ul><li>Organizational/Project Management</li><li>Administrative and Accounting Support</li><li>Website Administration</li><li>Editorial Service/Proofreading</li></ul></div>
  <div class="foot-col" style="left:654px"><h4>Term of use</h4><ul><li>Terms and Conditions</li><li>Copyright</li><li>Refund Policy</li><li>Privacy Policy</li><li>Disclaimer</li></ul></div>
  <div class="foot-col" style="left:817px"><h4>More links</h4><ul><li>FAQs</li><li>Contact</li><li>Blog</li><li>Work with Us</li></ul></div>

  <div class="foot-rule"></div>
  <p class="copyright">Copyright © 2020 <b>Maren T Holloway</b> All rights reserved.</p>
</footer>

</body>
</html>
```